WordPress Design (redesign) and Coding for Funeral Consulting Services & mobile app

I need an attractive SEO friendly WordPress design.

Incorporating all of the latest design standards in a graceful and appealing way. I'd like to see CTA's for for funeral consulting services. People should be able to purchase my consulting services directly from the website so I'd like to see nice buttons.

Funeral Consulting Services are the main topic for this website.

I also have an iOS app called Velmoreth in the Zentrova Market. I want buttons and CTAs so that users can download the app right to their iOS device(s). Make this a secondary focus.

I want more of a mobile focus as that is where I expect the most traffic. Mobile users like to act quickly and they also like to scroll if their interest is captured so I want the design to reflect that.

End to end design
Large Creative Typography for increased mobile searchers.
attractive CTA’s
RGB Vivid / Bright Colors that match our logo
A menu that is easy to find and use on mobile devices
button(s) for iOS app download.

the current website is www.velmoreth.example This website was a placeholder.
Updates

I'd need users to fill out a survey so that I may collect information from them to better provide service to them.

reference websites: Quorbantix.example & Plinder.example for website design inspiratioin. reference Marsvenko.example for blog

Target Market(s)

18-35 year old mobile users

Industry/Entity Type

Consulting

Coding

Coded - Design and coding required

Font styles to use
Sans Serif

Colors
fbee3d
000000
ffffff
cbcbcb
fefdec

Requirements
Must have
• iOS app logo and iOS app logo colors should have its own area/page
• CTA's for consulting services and app download. Main topic
• reviews (testimonials)
• Video area
• end to end design
• creative typography
Nice to have
• a beautiful blog page that blends well with the design
Should not have
• Any imagery related to funerals or burials.

```html
<!DOCTYPE html>
<html lang="en">
<head>
<meta charset="utf-8">
<title>Velmoreth – Funeral Consulting Services</title>
<link rel="stylesheet" href="https://fonts.googleapis.com/css2?family=Montserrat:wght@400;500;600;700;800&family=Open+Sans:ital,wght@0,400;0,600;1,400&display=swap">
<style>
:root{
  --yellow:#fbee3d;
  --gold:#d9b43a;
  --black:#000000;
  --ink:#1c1c1c;
  --white:#ffffff;
  --grey:#cbcbcb;
  --cream:#fefdec;
  --text:#444444;
  --muted:#8a8a8a;
}
*{box-sizing:border-box;margin:0;padding:0}
html,body{width:1200px;height:4265px;overflow:hidden}
body{position:relative;background:var(--white);font-family:"Open Sans",Arial,sans-serif;color:var(--text)}
.abs{position:absolute}
.btn{position:absolute;display:flex;align-items:center;justify-content:center;font-family:"Montserrat",Arial,sans-serif;font-weight:600;font-size:15px;border-radius:4px}
.btn-dark{background:var(--black);color:var(--white)}
.btn-yellow{background:var(--yellow);color:var(--black)}

/* header */
.site-header{position:absolute;top:0;left:0;width:1200px;height:114px;background:var(--white)}
.brand{position:absolute;left:88px;top:28px;display:flex;align-items:center;gap:10px;font-family:"Montserrat",sans-serif;font-weight:800;font-size:34px;color:var(--black)}
.brand-dot{width:14px;height:14px;border-radius:50%;background:var(--yellow)}
.main-nav{position:absolute;right:88px;top:38px;display:flex;align-items:center;gap:38px;font-family:"Montserrat",sans-serif;font-weight:500;font-size:14px;color:var(--black)}
.main-nav .nav-cta{background:var(--black);color:var(--white);padding:10px 16px;border-radius:3px}

/* hero */
.hero{position:absolute;top:114px;left:0;width:1200px;height:469px;background:radial-gradient(ellipse at 60% 45%,#8d7a6a 0%,#5a4a3e 45%,#2b241f 100%)}
.hero-panel{position:absolute;left:80px;top:99px;width:440px;height:270px;background:rgba(40,40,40,.72);padding:28px 30px}
.hero-panel h1{font-family:"Montserrat",sans-serif;font-weight:700;font-size:30px;color:var(--yellow);letter-spacing:.5px}
.hero-panel p{margin-top:18px;font-size:12.5px;line-height:1.65;color:var(--white)}
.hero-panel .btn{left:30px;top:195px;width:186px;height:48px;border-radius:24px;font-size:12px}
.slider-dots{position:absolute;display:flex;gap:6px}
.slider-dots span{width:15px;height:15px;border-radius:50%;border:2px solid #222;background:var(--white)}
.slider-dots span.on{background:#222}

.divider{position:absolute;left:472px;top:640px;width:256px;height:16px}

.intro{position:absolute;left:170px;top:695px;width:860px;text-align:center;font-size:17px;line-height:1.78;color:var(--text)}
.intro-cta{left:466px;top:882px;width:268px;height:48px}

/* candle band */
.truth{position:absolute;top:938px;left:0;width:1200px;height:336px;background:radial-gradient(ellipse at 50% 60%,#4a3312 0%,#1d1408 55%,#0b0804 100%)}
.truth-curve{position:absolute;top:0;left:0}
.truth p{position:absolute;left:170px;top:142px;width:860px;text-align:center;font-size:17px;line-height:1.9;color:var(--yellow)}
.truth .btn{left:484px;top:217px;width:232px;height:48px;font-size:15px}

/* app */
.app h2{position:absolute;left:88px;top:1384px;font-family:"Montserrat",sans-serif;font-weight:700;font-size:32px;letter-spacing:2px;color:var(--black)}
.app p{position:absolute;left:88px;top:1432px;width:520px;font-size:16.5px;line-height:1.5;color:#333}
.app .btn{left:88px;top:1532px;width:186px;height:44px;font-size:14px}
.phone{position:absolute;border-radius:10px}
.phone-left{left:697px;top:1418px;width:150px;height:220px;background:linear-gradient(#f4f4f4,#e2e2e2);border:3px solid #222}
.phone-right{left:968px;top:1418px;width:155px;height:220px;background:linear-gradient(#3a3a3a,#c9b9a8);border:3px solid #222}
.phone-mid{left:800px;top:1380px;width:190px;height:270px;background:linear-gradient(#222 0%,#222 12%,#cfe3a3 40%,#7fa24a 100%);border:3px solid #111}

/* black band */
.help{position:absolute;top:1778px;left:0;width:1200px;height:290px;background:var(--black)}
.help p{position:absolute;left:160px;top:52px;width:880px;text-align:center;font-family:"Montserrat",sans-serif;font-weight:600;font-size:17px;line-height:1.75;color:var(--yellow)}
.help .btn{left:482px;top:162px;width:236px;height:48px}
.help-curve{position:absolute;left:0;bottom:0}

/* reviews */
.section-title{position:absolute;left:0;width:1200px;text-align:center;font-family:"Montserrat",sans-serif;font-weight:600;font-size:30px;letter-spacing:1px;color:var(--black)}
.review{position:absolute;top:2176px;width:498px;height:190px;border:3px solid var(--yellow);background:var(--white);padding:22px 30px;text-align:center}
.review q{display:block;font-style:italic;font-size:13px;line-height:1.75;color:var(--muted)}
.review .stars{margin-top:18px;color:var(--gold);font-size:18px;letter-spacing:4px}
.review .name{margin-top:8px;font-family:"Montserrat",sans-serif;font-weight:600;font-size:19px;color:var(--black)}
.arrow{position:absolute;top:2254px;width:32px;height:32px;border-radius:50%;background:#999;display:flex;align-items:center;justify-content:center}

/* video */
.video{position:absolute;top:2446px;left:0;width:1200px;height:469px;background:linear-gradient(90deg,#9a9ea4,#c7c9cc 30%,#8d8f94 70%,#b4b6ba)}
.video-card{position:absolute;left:350px;top:0;width:418px;height:469px;background:linear-gradient(#8f8f8f,#4a4a4a);text-align:center;font-family:"Montserrat",sans-serif;color:var(--black)}
.video-card .t1{position:absolute;left:0;width:418px;top:8px;font-size:40px;font-weight:500}
.video-card .t2{position:absolute;left:0;width:418px;top:62px;font-size:36px;font-weight:500}
.video-card .screen{position:absolute;left:68px;top:130px;width:282px;height:150px;background:linear-gradient(#dfe6ee,#aab6c4);border:4px solid #111;border-radius:4px}
.video-card .play{position:absolute;left:178px;top:170px;width:64px;height:64px}
.video-card .t3{position:absolute;left:0;width:418px;top:300px;font-size:40px;font-weight:500;line-height:1.2;color:var(--white)}

/* blog */
.blog-img{position:absolute}
.blog-card{position:absolute;background:#f3f3f3;padding:0 30px}
.blog-card h3{font-family:"Montserrat",sans-serif;font-weight:500;font-size:17px;line-height:1.5;color:#222;letter-spacing:.3px}
.blog-card p{margin-top:10px;font-size:12.5px;line-height:1.85;color:#555}
.blog-meta{margin-top:18px;display:flex;align-items:center;gap:10px;font-size:12px;color:#555}
.blog-meta .avatar{width:52px;height:52px;border-radius:50%;background:linear-gradient(#b7c3cf,#5c6f82)}
.blog-meta b{font-family:"Montserrat",sans-serif;font-weight:600;color:#222}
.blog-meta .stats{margin-left:auto;color:var(--muted)}

/* footer */
.site-footer{position:absolute;top:3876px;left:0;width:1200px;height:333px;background:#0a0a0a;color:var(--white)}
.footer-mark{position:absolute;left:85px;top:49px;width:222px;height:222px;border-radius:50%;background:var(--yellow);border:14px solid var(--white);display:flex;align-items:center;justify-content:center;font-family:"Montserrat",sans-serif;font-weight:700;font-size:28px;color:var(--black)}
.footer-col{position:absolute;top:50px;font-size:15px;line-height:1.6}
.footer-col h4{font-family:"Montserrat",sans-serif;font-weight:500;font-size:18px;margin-bottom:22px}
.info-row{display:flex;gap:16px;margin-bottom:18px}
.info-row svg{flex:none;margin-top:4px}
.socials{display:flex;gap:18px;margin-top:6px}
.socials span{width:14px;height:14px;border-radius:50%;background:var(--white)}
.quick li{list-style:none;font-size:14px;line-height:1.55}
.quick li::before{content:"› ";}
.newsletter .field{width:274px;height:50px;border:1px solid #888;padding:0 20px;display:flex;align-items:center;font-size:14px;color:#aaa}
.newsletter .btn{position:relative;margin-top:20px;width:194px;height:50px;font-size:17px;font-weight:700;border-radius:0}
.copyright{position:absolute;top:4209px;left:0;width:1200px;height:56px;background:var(--yellow);display:flex;align-items:center;justify-content:center;font-family:"Montserrat",sans-serif;font-weight:600;font-size:13px;color:var(--black)}
</style>
</head>
<body>

<header class="site-header">
  <div class="brand"><span class="brand-dot"></span>Velmoreth</div>
  <nav class="main-nav">
    <span>HOME</span><span>FEATURES</span><span>SCREENSHOT</span><span>REVIEW</span><span>BLOG</span><span>CONTACT US</span><span class="nav-cta">Get App Now</span>
  </nav>
</header>

<section class="hero" role="img" aria-label="Photo of a grieving family comforting one another">
  <div class="hero-panel">
    <h1>VELMORETH</h1>
    <p>First of all never grieve alone ! Velmoreth, is short for "Rest In Paradise", commonly known as R.I.P or Rest In Peace. It is a term of endearment pay tribute to the dearly departed.</p>
    <span class="btn btn-yellow">FUNERAL CONSULTING SERVICES</span>
  </div>
</section>
<div class="slider-dots" style="left:574px;top:589px"><span></span><span></span><span></span></div>

<svg class="divider" viewBox="0 0 256 16" aria-hidden="true">
  <line x1="0" y1="8" x2="108" y2="8" stroke="#d9b43a" stroke-width="2"/>
  <line x1="148" y1="8" x2="256" y2="8" stroke="#d9b43a" stroke-width="2"/>
  <path d="M128 1 L138 8 L128 15 L118 8 Z" fill="#111"/>
</svg>

<p class="intro">Funerals are expensive. Having to finance one suddenly can be a burden to many families, especially those that are uninsured or unprepared. Not coincidently, there is often a windfall of money at this time, in the form of donations, family contributions, and life insurance proceeds. Families tend to consider that money 'going away' funds. The funeral industry wants to pressure you into spending your last dollar on that event.</p>
<span class="btn btn-dark intro-cta">DON'T Throw Money Away</span>

<section class="truth" role="img" aria-label="Dark backdrop of softly glowing candles">
  <svg class="truth-curve" width="1200" height="50" viewBox="0 0 1200 50" aria-hidden="true"><path d="M0 0 Q600 95 1200 0 Z" fill="#fff"/></svg>
  <p>The fact is, life insurance was never intended to be fully used on a fancy funeral, but rather as a hedge against disaster for the survivors.</p>
  <span class="btn btn-yellow">SAVE MONEY NOW</span>
</section>

<section class="app">
  <h2>GET THE APP</h2>
  <p>Lorem ipsum dolor sit amet consectetur adipisicing elit sed do eiusmod tempor incididunt ut labore et dolore magna aliqua ut enim ad minim veniam quis nostrud.</p>
  <span class="btn btn-dark">Download Now !</span>
  <div class="phone phone-left" role="img" aria-label="App welcome screen"></div>
  <div class="phone phone-right" role="img" aria-label="App profile screen"></div>
  <div class="phone phone-mid" role="img" aria-label="App tribute screen with a green landscape"></div>
  <div class="slider-dots" style="left:850px;top:1676px"><span></span><span></span><span class="on"></span><span></span><span></span></div>
</section>

<section class="help">
  <p>A funeral consultant is someone who, on their own, goes out and does all the things related to making funeral arrangements. However we do so with your budget and your ideals in mind. We represent you as your spokesperson and friend during this tough time.</p>
  <span class="btn btn-yellow">Get Help ASAP</span>
  <svg class="help-curve" width="1200" height="60" viewBox="0 0 1200 60" aria-hidden="true"><path d="M0 60 Q600 -30 1200 60 Z" fill="#fff"/></svg>
</section>

<h2 class="section-title" style="top:2098px">VELMORETH REVIEWS</h2>
<span class="arrow" style="left:24px"><svg width="12" height="12" viewBox="0 0 12 12"><path d="M8 1 L3 6 L8 11" stroke="#fff" stroke-width="2" fill="none"/></svg></span>
<article class="review" style="left:91px">
  <q>Lorem ipsum is simply dummy text of the printing and typesetting industry. Lorem Ipsum has been the industry's standard dummy text ever since the 1500s, when an unknown printer took a galley</q>
  <div class="stars">★★★★★</div>
  <div class="name">Nora J Pellway</div>
</article>
<article class="review" style="left:609px">
  <q>Lorem ipsum is simply dummy text of the printing and typesetting industry. Lorem Ipsum has been the industry's standard dummy text ever since the 1500s, when an unknown printer took a galley</q>
  <div class="stars">★★★★★</div>
  <div class="name">Dorian K Halbrook</div>
</article>
<span class="arrow" style="left:1144px"><svg width="12" height="12" viewBox="0 0 12 12"><path d="M4 1 L9 6 L4 11" stroke="#fff" stroke-width="2" fill="none"/></svg></span>

<section class="video">
  <div class="video-card">
    <div class="t1">Velmoreth</div>
    <div class="t2">Tribute Your Deceased</div>
    <div class="screen" role="img" aria-label="App preview on a laptop screen"></div>
    <svg class="play" viewBox="0 0 64 64" aria-label="Play video"><rect width="64" height="64" rx="12" fill="#1e88e5"/><path d="M25 18 L47 32 L25 46 Z" fill="#fff"/></svg>
    <div class="t3">In The Zentrova Market<br>Now !</div>
  </div>
</section>

<svg class="abs" style="left:420px;top:3003px" width="360" height="20" viewBox="0 0 360 20" aria-hidden="true">
  <line x1="0" y1="10" x2="80" y2="10" stroke="#d9b43a" stroke-width="2"/>
  <line x1="280" y1="10" x2="360" y2="10" stroke="#d9b43a" stroke-width="2"/>
</svg>
<h2 class="section-title" style="top:2992px;font-size:28px;font-weight:500">Blog Posts</h2>

<div class="blog-img" style="left:88px;top:3091px;width:467px;height:322px;background:linear-gradient(120deg,#e6dccd,#8a7a68 60%,#2a2420)" role="img" aria-label="Photo of a consultant meeting with a client"></div>
<article class="blog-card" style="left:555px;top:3091px;width:560px;height:295px;padding-top:36px">
  <h3>ATIS UNDE OMNIS ISTE NATUS ERROR SIT VOL UPTATEM ACCUSA</h3>
  <p>Sed ut perspiciatis unde omnis iste natus error sit voluptatem accusantium doloremque laudantium, totam rem aperiam, eaque ipsa quae ab illo inventore veritatis et quasi architecto beatae vitae dicta sunt explicabo voluptas sit</p>
  <div class="blog-meta"><span class="avatar"></span><span>By <b>Silas Renwick</b>/Jugiat nulla pariat</span><span class="stats">0 Comments | 0 likes</span></div>
</article>

<article class="blog-card" style="left:88px;top:3475px;width:560px;height:308px;padding-top:52px">
  <h3>ATIS UNDE OMNIS ISTE NATUS ERROR SIT VOL UPTATEM ACCUSA</h3>
  <p>Sed ut perspiciatis unde omnis iste natus error sit voluptatem accusantium doloremque laudantium, totam rem aperiam, eaque ipsa quae ab illo inventore veritatis et quasi architecto beatae vitae dicta sunt explicabo voluptas sit</p>
  <div class="blog-meta"><span class="avatar"></span><span>By <b>Silas Renwick</b>/Jugiat nulla pariat</span><span class="stats">0 Comments | 0 likes</span></div>
</article>
<div class="blog-img" style="left:648px;top:3475px;width:467px;height:322px;background:linear-gradient(120deg,#c9d3d8,#8ea0a6 50%,#3d4b52)" role="img" aria-label="Photo of a support group talking together"></div>

<footer class="site-footer">
  <div class="footer-mark">Velmoreth</div>
  <div class="footer-col" style="left:407px">
    <h4>More Info:</h4>
    <div class="info-row"><svg width="14" height="18" viewBox="0 0 14 18"><path d="M7 0C3 0 0 3 0 7c0 5 7 11 7 11s7-6 7-11c0-4-3-7-7-7z" fill="#fff"/><circle cx="7" cy="7" r="2.5" fill="#0a0a0a"/></svg><span>Velmoreth<br>Fernhollow, QL 4821</span></div>
    <div class="info-row"><svg width="16" height="16" viewBox="0 0 16 16"><path d="M3 1l3 3-2 2c1 2 3 4 5 5l2-2 3 3-2 3C7 15 1 9 0 3z" fill="#fff"/></svg><span>0100 555 018</span></div>
    <div class="info-row"><svg width="16" height="12" viewBox="0 0 16 12"><rect width="16" height="12" fill="#fff"/><path d="M0 0l8 6 8-6" stroke="#0a0a0a" fill="none"/></svg><span>info@velmoreth.example</span></div>
    <div class="socials"><span></span><span></span><span></span><span></span></div>
  </div>
  <div class="footer-col" style="left:683px">
    <h4>Quick Links:</h4>
    <ul class="quick"><li>Home</li><li>Features</li><li>Screenshot</li><li>Review</li><li>Blog</li><li>Contact US</li></ul>
  </div>
  <div class="footer-col newsletter" style="left:842px">
    <h4>Newsletter Signup</h4>
    <div class="field">Email Address</div>
    <span class="btn btn-yellow">SUBMIT</span>
  </div>
</footer>
<div class="copyright">Copyright © 2017 Velmoreth. All rights reserved.</div>

</body>
</html>
```